Business Card Re-Design...or logo does not look sharp

Hello

We are a start-up and just need someone to help us.

Our colors are: Marlowe Hush pink (yeah I know) and charcoal for the lettering.

I am attaching our logo which needs cleaning up.

We want the JUST the lady ironing on the table (pink) in front, and the background in charcoal. All the business info can be on the back.

Dims on card are 2 x 2''

Also, if you have better ideas....please let us know!

Thanks

Gregory

La Comadre Vapor
4827 Quellbrook Dr Suite B2
El Paso TX 79936
915-555-0148

```html
<!DOCTYPE html>
<html lang="en">
<head>
<meta charset="utf-8">
<title>La Comadre Vapor — Business Card</title>
<link rel="stylesheet" href="https://fonts.googleapis.com/css2?family=Marcellus+SC&display=swap">
<style>
  :root {
    --brand-pink: #ec1398;
    --name-pink: #e8119a;
    --charcoal: #4a4a4c;
    --ring-dark: #3a1f28;
    --ring-edge: #5a2a3c;
    --oval-black: #050304;
    --figure-pink: #e63ca6;
    --text-light: #ececec;
    --page: #ffffff;
  }
  * { margin: 0; padding: 0; box-sizing: border-box; }
  html, body {
    width: 980px;
    height: 1200px;
    overflow: hidden;
    background: var(--page);
  }
  .canvas {
    position: relative;
    width: 980px;
    height: 1200px;
  }
  .card-front {
    position: absolute;
    left: 21px;
    top: 0;
    width: 938px;
    height: 530px;
    background: var(--brand-pink);
  }
  .card-front svg {
    display: block;
    width: 100%;
    height: 100%;
  }
  .card-back {
    position: absolute;
    left: 18px;
    top: 552px;
    width: 938px;
    height: 529px;
    background: var(--charcoal);
  }
  .back-accent {
    position: absolute;
    left: 0;
    top: 418px;
    width: 100%;
    height: 19px;
    background: var(--brand-pink);
  }
  .business-info {
    position: absolute;
    right: 26px;
    top: 30px;
    text-align: right;
    font-family: "Marcellus SC", serif;
  }
  .business-name {
    font-size: 42px;
    line-height: 50px;
    font-weight: 400;
    color: var(--name-pink);
    letter-spacing: 0.5px;
  }
  .business-address {
    margin-top: 4px;
    font-style: normal;
    font-size: 28px;
    line-height: 37px;
    color: var(--text-light);
    letter-spacing: 0.5px;
  }
</style>
</head>
<body>
<main class="canvas">
  <section class="card-front" aria-label="Card front">
    <svg viewBox="0 0 938 530" xmlns="http://www.w3.org/2000/svg">
      <defs>
        <radialGradient id="ring-shade" cx="50%" cy="50%" r="50%">
          <stop offset="70%" stop-color="var(--ring-dark)"/>
          <stop offset="100%" stop-color="var(--ring-edge)"/>
        </radialGradient>
        <radialGradient id="figure-tone" cx="50%" cy="50%" r="60%">
          <stop offset="0%" stop-color="#f050b4"/>
          <stop offset="100%" stop-color="var(--figure-pink)"/>
        </radialGradient>
      </defs>
      <ellipse class="emblem-ring" cx="469" cy="266" rx="263" ry="213" fill="url(#ring-shade)"/>
      <ellipse class="emblem-oval" cx="469" cy="266" rx="195" ry="146" fill="var(--oval-black)"/>
      <rect class="emblem-figure" x="336" y="126" width="270" height="272" rx="30"
            fill="url(#figure-tone)" opacity="0.85"
            role="img" aria-label="Pink silhouette of a lady ironing at a table"/>
    </svg>
  </section>

  <section class="card-back" role="img" aria-label="Charcoal card back with faint floral pattern">
    <div class="business-info">
      <h1 class="business-name">La Comadre Vapor</h1>
      <address class="business-address">
        4827 Quellbrook Dr Suite<br>
        B2 El<br>
        Paso TX<br>
        79936 915-555-0148
      </address>
    </div>
    <div class="back-accent"></div>
  </section>
</main>
</body>
</html>
```